Opening Soon Hoarding Design for Retail Footwear Chain

TALVERNO is a retail footwear chain operating primarily in North America. It offers exclusive and non-exclusive brands for men and women.

We need an advertisement design announcing a store opening, to be placed on a hoarding.

A hoarding is a large board in an enclosed shopping center, used to display advertisements; similar to a billboard. It is a temporary board (or fence) erected in front of a retail site during the construction period.

The advertisement we need is to be placed on the hoarding that covers the store front facade during the construction period, and it is removed the night prior to opening day.

Attached are the TALVERNO store pictures, as well as the logo / pantone color document. The primary colors identifying TALVERNO are Rose gold, white, and red.

The objective or focus of the advertisement on the hoarding should include the following:
- TALVERNO (as per logo)
- Opening soon
- website : www.talverno.ca
- Facebook / Twitter
- A clearly identified section of the advertisement announcing that we are recruiting / looking for employees; this should be announced as: "Join the Talverno Family" and provide email: careers@talverno.ca

Target Market(s)

Women & men between the approx ages of 25 to 65. The age group is quite wide because the product range we have in the store is very diverse too.

Industry/Entity Type

Retail

Requirements
Must have
• 1- Talverno name / logo
• 2- Opening soon
• 3- website: www.talverno.ca (& Facebook / twitter reference)
• 4- Join the Talverno Family: careers@talverno.ca
• Main objective: To have a design that will intrigue people walking in a shopping mall enough for them to stop for a second and look at the ad design. (At the end of the day, that's the main objective of a hoarding design - to get people's attention).
Nice to have
• I can give you an approx. SIZE, but I would like a design that can be slightly modified for printing purposes, as the hoarding size from 1 store to the next will not be identical. However, I would like to use the same design for all hoardings.
• With that said, the approx hoarding size would be 15 feet wide and 10 feet high.
• Some other hoardings will be slightly bigger in width (going up to 20 ft max) but the height should be fairly standard.
Should not have
• The end design should not have a picture / design of the store as per the attached images. The store design and how it looks should be a surprise for the customers.

```html
<!DOCTYPE html>
<html lang="en">
<head>
<meta charset="utf-8">
<title>Talverno – Opening Soon Hoarding</title>
<link rel="stylesheet" href="https://fonts.googleapis.com/css2?family=Cinzel:wght@700&family=Questrial&display=swap">
<style>
  :root {
    --stage: #1b1b1b;
    --brand-red: #a91e24;
    --band-red: #640006;
    --dotted-red: #e0343b;
    --pattern-red: #9c1a20;
    --white: #ffffff;
  }
  * { margin: 0; padding: 0; box-sizing: border-box; }
  html, body {
    width: 1200px;
    height: 1000px;
    overflow: hidden;
    background: var(--stage);
  }
  .hoarding {
    position: absolute;
    left: 170px;
    top: 212px;
    width: 860px;
    height: 575px;
    background: var(--brand-red);
    overflow: hidden;
    color: var(--white);
  }
  .footprint-pattern {
    position: absolute;
    left: 0;
    top: 215px;
    width: 100%;
    height: 360px;
    background: radial-gradient(ellipse at 50% 40%, var(--brand-red) 0%, var(--pattern-red) 100%);
  }
  .brand-name {
    position: absolute;
    top: 66px;
    width: 100%;
    text-align: center;
    font-family: "Questrial", sans-serif;
    font-size: 40px;
    letter-spacing: 6px;
    line-height: 1;
  }
  .opening-band {
    position: absolute;
    top: 135px;
    left: 0;
    width: 100%;
    height: 80px;
    background: var(--band-red);
  }
  .opening-band::before,
  .opening-band::after {
    content: "";
    position: absolute;
    left: 105px;
    right: 100px;
    border-top: 1px dotted var(--dotted-red);
  }
  .opening-band::before { top: 0; }
  .opening-band::after { bottom: 0; }
  .opening-title {
    position: absolute;
    top: 0;
    width: 100%;
    line-height: 80px;
    text-align: center;
    font-family: "Cinzel", serif;
    font-weight: 700;
    font-size: 70px;
    letter-spacing: 1px;
  }
  .pointer-arrows {
    position: absolute;
    left: 0;
    top: 225px;
    width: 860px;
    height: 70px;
  }
  .website {
    position: absolute;
    top: 280px;
    width: 100%;
    text-align: center;
    font-family: "Cinzel", serif;
    font-weight: 700;
    font-size: 33px;
    letter-spacing: 1px;
    line-height: 1.2;
  }
  .social-links {
    position: absolute;
    top: 337px;
    left: 370px;
    display: flex;
    gap: 26px;
  }
  .social-circle {
    width: 50px;
    height: 50px;
    border: 1.5px solid var(--white);
    border-radius: 50%;
  }
  .careers {
    position: absolute;
    top: 482px;
    width: 100%;
    text-align: center;
    font-family: "Questrial", sans-serif;
    font-size: 24px;
    line-height: 30px;
  }
</style>
</head>
<body>
  <main class="hoarding">
    <div class="footprint-pattern" role="img" aria-label="Faint pattern of red footprints walking in curving paths"></div>

    <h1 class="brand-name">TALVERNO</h1>

    <div class="opening-band">
      <p class="opening-title">OPENING SOON</p>
    </div>

    <svg class="pointer-arrows" viewBox="0 0 860 70" aria-hidden="true">
      <g fill="none" stroke="#ffffff" stroke-width="2" stroke-linecap="round">
        <path d="M184 6 C176 30 186 50 208 56"/>
        <path d="M196 46 L208 56 L194 59"/>
        <path d="M680 6 C688 30 678 50 656 56"/>
        <path d="M668 46 L656 56 L670 59"/>
      </g>
    </svg>

    <p class="website">WWW.TALVERNO.CA</p>

    <div class="social-links" aria-label="Social media links">
      <span class="social-circle"></span>
      <span class="social-circle"></span>
    </div>

    <p class="careers">Join the Talverno Family<br>careers@talverno.ca</p>
  </main>
</body>
</html>
```